Beacon Law Stationary - Law Firm

I am looking for a designer who can help me design letterhead and envelopes consistent with our new business cards. Feel free to reach out to me directly at ned@beaconlawgroup.example. Thank you!! Visit beaconlawgroup.example to see our site and the attached files for creative assets.

Target Market(s)

Anyone needing a lawyer

Font styles to use
Other font styles liked:
• Adobe Caslon Pro

Requirements
Must have
• Adobe Caslon Pro font
Full color
Nice to have
• My photo on front along with 2/3 face of camo - see mock up for example of what I have in mind.

American colors - similar to the ones found on my website and gold.

```html
<!DOCTYPE html>
<html lang="en">
<head>
<meta charset="utf-8">
<title>Beacon Law Letterhead</title>
<link href="https://fonts.googleapis.com/css2?family=Lato:wght@400;700&family=Roboto:wght@400&display=swap" rel="stylesheet">
<style>
  :root {
    --backdrop: #e8e8e8;
    --paper: #ffffff;
    --gold: #b29a57;
    --navy: #10233f;
    --ink: #3a3a3a;
    --body-text: #8e8e8e;
    --contact-text: #3c3c3c;
    --rule: #c9b77f;
    --signature-fill: #e6e6e6;
  }
  * { margin: 0; padding: 0; box-sizing: border-box; }
  html, body {
    width: 1195px; height: 1200px; overflow: hidden;
    background: var(--backdrop);
  }
  .letterhead {
    position: absolute; left: 147px; top: 18px;
    width: 900px; height: 1164px;
    background: var(--paper);
    font-family: "Lato", sans-serif;
  }
  .brand {
    position: absolute; left: 74px; top: 108px;
    font-family: "Lato", sans-serif;
    font-weight: 700; font-size: 28px; letter-spacing: 0;
    color: var(--navy); line-height: 1;
    display: flex; align-items: center; gap: 12px;
  }
  .brand-mark {
    width: 26px; height: 26px; background: var(--gold);
  }
  .contact {
    position: absolute; top: 102px;
    font-family: "Roboto", sans-serif; font-size: 12.5px; font-style: normal;
    line-height: 16.5px; color: var(--contact-text);
  }
  .contact-address { left: 480px; }
  .contact-divider {
    position: absolute; left: 651px; top: 97px;
    width: 1px; height: 46px; background: var(--rule);
  }
  .contact-lines { left: 670px; list-style: none; }
  .contact-lines li { display: flex; align-items: center; gap: 7px; }
  .contact-lines svg { width: 10px; height: 10px; fill: var(--gold); flex: none; }
  .salutation {
    position: absolute; left: 85px; top: 350px;
    font-weight: 700; font-size: 18.5px; color: var(--ink);
  }
  .letter-date {
    position: absolute; right: 89px; top: 350px;
    font-size: 18.5px; color: #707070;
  }
  .letter-body {
    position: absolute; left: 83px; top: 418px; width: 731px;
    font-size: 15.8px; letter-spacing: 0.25px; line-height: 33px; color: var(--body-text);
    text-align: justify;
  }
  .letter-body p + p { margin-top: 33px; }
  .signature {
    position: absolute; left: 83px; top: 936px;
    width: 178px; height: 50px; background: var(--signature-fill);
    border-radius: 4px;
  }
  .footer-band {
    position: absolute; left: 0; bottom: 0; width: 100%; height: 17px;
    background: var(--navy);
  }
</style>
</head>
<body>
<main class="letterhead">
  <header>
    <div class="brand"><span class="brand-mark"></span>Beacon Law</div>
    <address class="contact contact-address">
      48 Harbor Lantern Avenue<br>Brookhaven<br>Ohio 43210
    </address>
    <div class="contact-divider"></div>
    <ul class="contact contact-lines">
      <li><svg viewBox="0 0 10 10"><path d="M2 0.5l2 2-1 1.2a6 6 0 0 0 3.3 3.3l1.2-1 2 2-1.3 1.5C4.5 9.5 0.5 5.5 0.5 1.8z"/></svg>(555) 014-2290</li>
      <li><svg viewBox="0 0 10 10"><path d="M0.5 2h9v6h-9z M0.5 2l4.5 3.5 4.5-3.5" fill="none" stroke="#b29a57" stroke-width="1.2"/></svg>mara@beaconlawgroup.example</li>
      <li><svg viewBox="0 0 10 10"><circle cx="5" cy="5" r="4.2" fill="none" stroke="#b29a57" stroke-width="1"/><path d="M0.8 5h8.4M5 0.8c-2.4 2.6-2.4 5.8 0 8.4M5 0.8c2.4 2.6 2.4 5.8 0 8.4" fill="none" stroke="#b29a57" stroke-width="0.8"/></svg>www.beaconlawgroup.example</li>
    </ul>
  </header>

  <p class="salutation">Dear Mr. Smith,</p>
  <p class="letter-date">Oct. 20, 2021</p>

  <section class="letter-body">
    <p>Lorem ipsum dolor sit amet, consectetur adipiscing elit, sed do eiusmod tempor incididunt ut labore et dolore magna aliqua. Ut enim ad minim veniam, quis nostrud exercitation ullamco laboris nisi ut aliquip ex ea commodo consequat. Duis aute irure dolor in reprehenderit in voluptate velit esse cillum dolore eu fugiat nulla pariatur. Excepteur sint occaecat cupidatat non proident, sunt in culpa qui officia deserunt mollit anim id est laborum.</p>
    <p>Lorem ipsum dolor sit amet, consectetur adipiscing elit, sed do eiusmod tempor incididunt ut labore et dolore magna aliqua. Ut enim ad minim veniam, quis nostrud exercitation ullamco laboris nisi ut aliquip ex ea commodo consequat. Duis aute irure dolor in reprehenderit in voluptate velit esse cillum dolore eu fugiat nulla pariatur. Excepteur sint occaecat cupidatat non proident, sunt in culpa qui officia deserunt mollit anim id est laborum.Lorem ipsum dolor sit amet, consectetur adipiscing elit, sed do eiusmod tempor incididunt ut labore et dolore magna aliqua. Ut enim ad minim veniam, quis nostrud exercitation consectetur adipiscing elit, sed do eiusmod tempor incididunt ut labore et dolore magna aliqua. Ut enim ad minim veniam, quis nostrud exercitation.</p>
  </section>

  <div class="signature" role="img" aria-label="Handwritten signature"></div>

  <div class="footer-band"></div>
</main>
</body>
</html>
```